Graphic profile - "Winter Wonderland" Event

We are producing a event this upcoming christmas season, and we need a graphic design for it. The theme is; Winter Wonderland, and we would like to see designs that use the colors gold and blue, as well as white.
Magical, elegant and exclusive.

We need;
- A poster
- Invitations and envelope design
- Tickets (PVC Card) Three different packages + VIP; gold, silver and bronze.
- Bar menu

Industry/Entity Type

Entertainment Industry

Font styles to use
Serif
Script

Colors
0655a3
33a6d7
ffffff
fece3e

Requirements
Must have
• - Gold and sparkles
• TEXT
• Name of the event:
• The Velvet Lantern Soirée
• Et revolusjonerende dinnershow i magiske omgivelser
• More space for text.
• Bestill dine billetter i dag! (Header; Order your tickets today!)
• Gå inn på våre hjemmesider for å reservere deres billetter, eller ta kontakt med kundeservice på 947 81 452. ( Order your tickets online, or call customer service)

```html
<!DOCTYPE html>
<html lang="no">
<head>
<meta charset="utf-8">
<title>The Velvet Lantern Soirée – Poster</title>
<link href="https://fonts.googleapis.com/css2?family=Cinzel:wght@400;500&family=Josefin+Sans:wght@300;400&family=Poiret+One&display=swap" rel="stylesheet">
<style>
  :root {
    --night-deep: #0b1630;
    --night: #142349;
    --night-mid: #1d3160;
    --gold-light: #fce7a3;
    --gold: #e8c15a;
    --gold-dark: #b8872a;
    --white: #ffffff;
    --moon-top: #2c4a86;
    --moon-bottom: #16295a;
  }
  html, body {
    margin: 0;
    padding: 0;
    overflow: hidden;
    background: var(--night-deep);
  }
  .poster {
    position: relative;
    width: 849px;
    height: 1200px;
    overflow: hidden;
    background: linear-gradient(180deg, var(--night-deep) 0%, var(--night) 45%, var(--night-mid) 100%);
  }
  .night-sky {
    position: absolute;
    inset: 0;
    background:
      radial-gradient(ellipse 420px 140px at 30% 8%, rgba(90,110,160,0.28), transparent 70%),
      radial-gradient(ellipse 380px 120px at 80% 22%, rgba(90,110,160,0.22), transparent 70%),
      radial-gradient(ellipse 460px 150px at 20% 70%, rgba(90,110,160,0.22), transparent 70%),
      radial-gradient(ellipse 400px 130px at 60% 90%, rgba(90,110,160,0.2), transparent 70%);
  }
  .moon {
    position: absolute;
    left: 398px;
    top: 652px;
    width: 566px;
    height: 566px;
    border-radius: 50%;
    background: radial-gradient(circle at 40% 35%, var(--moon-top) 0%, var(--moon-bottom) 100%);
    box-shadow: 0 0 60px rgba(80,130,210,0.35);
  }
  .title {
    position: absolute;
    top: 168px;
    left: 0;
    width: 100%;
    margin: 0;
    text-align: center;
    font-family: "Cinzel", serif;
    font-weight: 500;
    font-size: 64px;
    line-height: 1.35;
    letter-spacing: 1px;
    background: linear-gradient(180deg, var(--gold-light) 0%, var(--gold) 50%, var(--gold-dark) 100%);
    -webkit-background-clip: text;
    background-clip: text;
    color: transparent;
  }
  .title .cap { font-size: 88px; }
  .rule {
    position: absolute;
    left: 160px;
    width: 584px;
    height: 1px;
    background: rgba(255,255,255,0.7);
  }
  .rule--top { top: 442px; }
  .rule--bottom { top: 500px; }
  .tagline {
    position: absolute;
    top: 454px;
    left: 0;
    width: 100%;
    margin: 0;
    text-align: center;
    font-family: "Poiret One", sans-serif;
    font-size: 25px;
    letter-spacing: 1px;
    color: var(--white);
  }
  .cta {
    position: absolute;
    top: 514px;
    left: 0;
    width: 100%;
    margin: 0;
    text-align: center;
    font-family: "Josefin Sans", sans-serif;
    font-weight: 400;
    font-size: 36px;
    letter-spacing: 1px;
    color: var(--white);
  }
  .booking-info {
    position: absolute;
    top: 842px;
    right: 36px;
    width: 400px;
    margin: 0;
    text-align: right;
    font-family: "Josefin Sans", sans-serif;
    font-weight: 300;
    font-size: 28px;
    line-height: 1.3;
    color: var(--white);
  }
</style>
</head>
<body>
  <main class="poster">
    <div class="night-sky" role="img" aria-label="Night sky with soft drifting clouds and scattered stars"></div>
    <div class="moon"></div>

    <h1 class="title"><span class="cap">T</span>HE <span class="cap">V</span>ELVET<br><span class="cap">L</span>ANTERN <span class="cap">S</span>OIRÉE</h1>

    <div class="rule rule--top"></div>
    <p class="tagline">ET REVOLUSJONERENDE DINNERSHOW I MAGISKE OMGIVELSER</p>
    <div class="rule rule--bottom"></div>

    <p class="cta">BESTILL DINE BILLETTER I DAG!</p>

    <p class="booking-info">Gå inn på våre hjemmesider for å reservere deres billetter, eller ta kontakt med kundeservice på 947 81 452</p>
  </main>
</body>
</html>
```